La Paloma Taberna

We need layouts for the attached 6 pages. The elements that are within the PDF are to be included in the design but their placement, the colors, everything that is there is completely up to your design ability so please get creative.
We like clean, web 2.0 type designs. Here is a restaurant with a nice design:http://tierrasolferino.example/ It does not need to be like this at all, just for a concept of what we like.
The logo on the top left of the site is our logo. I've attached it and a PDF containing the elements of the site here.

```html
<!DOCTYPE html>
<html lang="en">
<head>
<meta charset="utf-8">
<title>La Paloma Taberna — Home</title>
<link href="https://fonts.googleapis.com/css2?family=Open+Sans:wght@400;600;700&display=swap" rel="stylesheet">
<style>
  :root {
    --header-bg: #262626;
    --footer-bg: #2b2b2b;
    --gold: #c8963a;
    --gold-light: #f3cf6a;
    --panel-top: #e6c97e;
    --panel-bottom: #d1aa55;
    --ink: #6a6a6a;
    --ink-dark: #2a2622;
    --nav-text: #e6e6e6;
    --footer-text: #bdbdbd;
    --rule: #4a4a4a;
    --white: #ffffff;
  }
  * { box-sizing: border-box; margin: 0; padding: 0; }
  html, body { width: 1070px; height: 1200px; overflow: hidden; background: var(--white); }
  body { font-family: "Open Sans", sans-serif; position: relative; }
  .page { position: relative; width: 1070px; height: 1200px; overflow: hidden; }

  .site-header { position: absolute; left: 0; top: 0; width: 1070px; height: 189px; background: var(--header-bg); }
  .brand { position: absolute; left: 89px; top: 104px; display: flex; align-items: center; gap: 12px; }
  .brand-mark { width: 26px; height: 26px; background: var(--gold); }
  .brand-name { font-size: 25px; font-weight: 600; color: var(--white); letter-spacing: 0.3px; }

  .social { position: absolute; top: 56px; left: 784px; display: flex; gap: 12px; }
  .social span { width: 30px; height: 30px; border-radius: 50%; display: block; }
  .social .s1 { background: #3b5a9a; }
  .social .s2 { background: #2aa3e0; }
  .social .s3 { background: #5b7f9e; }
  .social .s4 { background: #cf2a1c; }
  .social .s5 { background: #3a4f8e; }

  .main-nav { position: absolute; top: 141px; left: 478px; font-size: 14px; text-transform: uppercase; }
  .main-nav a { position: absolute; color: var(--nav-text); text-decoration: none; white-space: nowrap; }
  .main-nav a.current { color: var(--gold-light); }

  .reservation { position: absolute; left: 90px; top: 205px; width: 231px; height: 255px;
    background: linear-gradient(180deg, var(--panel-top), var(--panel-bottom)); }
  .reservation h2 { position: absolute; left: 14px; top: 17px; font-size: 17px; font-weight: 700; color: var(--white);
    text-transform: uppercase; letter-spacing: -0.1px; white-space: nowrap; line-height: 22px; }
  .field { position: absolute; left: 14px; width: 203px; height: 37px; background: var(--white); border-radius: 2px; display: flex;
    align-items: center; justify-content: space-between; padding: 0 8px 0 11px; font-size: 12px; color: #555; }
  .field-date { top: 52px; }
  .field-time { top: 99px; }
  .field-party { top: 146px; }
  .find-table { position: absolute; right: 14px; top: 202px; width: 120px; height: 33px; background: var(--ink-dark);
    color: var(--gold-light); font-size: 14px; border-radius: 2px; display: flex; align-items: center; justify-content: center; }

  .slider { position: absolute; left: 326px; top: 205px; width: 655px; height: 255px;
    background: radial-gradient(ellipse at 30% 70%, #d8c7b0 0%, #8a6a48 28%, #3a4a5c 60%, #1c1a18 100%); }
  .slider-caption { position: absolute; left: 129px; top: 10px; font-size: 19px; font-weight: 600; color: var(--gold-light); }
  .slider-arrow { position: absolute; top: 115px; width: 24px; height: 24px; }
  .slider-arrow.prev { left: 18px; }
  .slider-arrow.next { right: 19px; }

  .promo { position: absolute; left: 90px; width: 231px; }
  .promo-race { top: 477px; height: 277px; background: linear-gradient(180deg, #9fb2a0 0%, #d9dcd6 55%, #f2f2f2 78%, #0f1a24 78%, #0f1a24 100%); }
  .promo-conference { top: 766px; height: 276px; border: 3px solid #4a4a4a;
    background: linear-gradient(180deg, #ffffff 0%, #ffffff 45%, #a8dbe3 45%, #a8dbe3 65%, #ffffff 65%, #b9d98c 88%, #d9d2bf 100%); }

  .welcome { position: absolute; left: 344px; top: 478px; width: 637px; }
  .welcome h1 { font-size: 22px; font-weight: 700; color: var(--gold); margin-bottom: 14px; }
  .welcome p { font-size: 12.3px; line-height: 18.6px; color: var(--ink); margin-bottom: 9.3px; }

  .site-footer { position: absolute; left: 0; top: 1070px; width: 1070px; height: 130px; background: var(--footer-bg); }
  .footer-nav { position: absolute; top: 26px; left: 0; width: 1070px; font-size: 13px; }
  .footer-nav a { position: absolute; color: var(--footer-text); text-decoration: none; white-space: nowrap; }
  .footer-nav a::before { content: "• "; font-size: 9px; vertical-align: 2px; color: #8a8a8a; }
  .footer-rule { position: absolute; left: 89px; top: 62px; width: 892px; height: 1px; background: var(--rule); }
  .copyright { position: absolute; top: 85px; left: 0; width: 1070px; text-align: center; font-size: 13px; color: var(--footer-text); }
</style>
</head>
<body>
<div class="page">
  <header class="site-header">
    <div class="brand"><span class="brand-mark"></span><span class="brand-name">La Paloma Taberna</span></div>
    <div class="social" aria-label="Social links">
      <span class="s1" role="img" aria-label="Social network link"></span>
      <span class="s2" role="img" aria-label="Social network link"></span>
      <span class="s3" role="img" aria-label="Photo sharing link"></span>
      <span class="s4" role="img" aria-label="Reviews link"></span>
      <span class="s5" role="img" aria-label="Listing badge"></span>
    </div>
    <nav class="main-nav">
      <a class="current" style="left:0">Home</a>
      <a style="left:78px">Menu</a>
      <a style="left:157px">Contact</a>
      <a style="left:257px">Calendar</a>
      <a style="left:367px">Press</a>
      <a style="left:443px">Gallery</a>
    </nav>
  </header>

  <section class="reservation">
    <h2>Make a Reservation</h2>
    <div class="field field-date"><span>19-Jun-14</span>
      <svg width="26" height="22" viewBox="0 0 26 22"><rect x="1" y="3" width="24" height="18" fill="none" stroke="#aaa" stroke-width="1.5"/><rect x="1" y="3" width="24" height="4" fill="#bbb"/><g fill="#bbb"><rect x="4" y="9" width="4" height="3"/><rect x="11" y="9" width="4" height="3"/><rect x="18" y="9" width="4" height="3"/><rect x="4" y="15" width="4" height="3"/><rect x="11" y="15" width="4" height="3"/><rect x="18" y="15" width="4" height="3"/></g></svg>
    </div>
    <div class="field field-time"><span>07:00 PM</span>
      <svg width="26" height="26" viewBox="0 0 26 26"><circle cx="13" cy="13" r="11.5" fill="none" stroke="#aaa" stroke-width="1.5"/><path d="M13 6v7l5 3" fill="none" stroke="#aaa" stroke-width="1.5"/></svg>
    </div>
    <div class="field field-party"><span>2 People</span>
      <svg width="26" height="26" viewBox="0 0 26 26"><circle cx="13" cy="8" r="6" fill="#bbb"/><path d="M2 26c0-8 5-11 11-11s11 3 11 11z" fill="#bbb"/></svg>
    </div>
    <div class="find-table">FIND A TABLE</div>
  </section>

  <section class="slider" role="img" aria-label="Photo of a plated salad and wine glasses on a dim restaurant table">
    <div class="slider-caption">Proin tempus magna ligula</div>
    <svg class="slider-arrow prev" viewBox="0 0 24 24"><circle cx="12" cy="12" r="12" fill="#fff"/><path d="M14.5 8v8l-6-4z" fill="#222"/></svg>
    <svg class="slider-arrow next" viewBox="0 0 24 24"><circle cx="12" cy="12" r="12" fill="#fff"/><path d="M9.5 8v8l6-4z" fill="#222"/></svg>
  </section>

  <div class="promo promo-race" role="img" aria-label="Advertisement for a triathlon race series with a runner photo"></div>
  <div class="promo promo-conference" role="img" aria-label="Advertisement poster for a conference with city skyline and register button"></div>

  <main class="welcome">
    <h1>Welcome to La Paloma Taberna</h1>
    <p>Proin tempus magna ligula, eget consequat risus dignissim eget. Phasellus placerat orci lectus, sit amet gravida leo vestibulum et. Etiam elit ligula, pulvinar vel libero vel, dignissim posuere nunc. In sit amet auctor lorem. Morbi sit amet tristique diam, sed blandit nisl. Ut mi felis, facilisis nec nunc eu, elementum euismod justo. Nullam eget nunc a massa venenatis suscipit. Morbi ultrices lacus libero, lacinia suscipit libero condimentum lacinia. Pellentesque sagittis sem a ipsum ullamcorper sodales. Aliquam sodales viverra turpis, at viverra enim tristique vitae. Ut posuere a lacus ac auctor. Etiam ligula nisi, consequat quis mollis ac, porta et felis. Phasellus fermentum aliquam neque vitae feugiat. Etiam odio tellus, ullamcorper id suscipit ut, pharetra vel tortor. Aliquam vitae ante eget felis accumsan ornare.</p>
    <p>Praesent laoreet libero id elit malesuada, vitae adipiscing quam imperdiet. Vivamus placerat dictum nisi, eget aliquam odio pellentesque id. Phasellus rhoncus magna eu mauris placerat varius. Fusce id orci sollicitudin arcu condimentum vulputate. Etiam iaculis eleifend quam. Cum sociis natoque penatibus et magnis dis parturient montes, nascetur ridiculus mus. Pellentesque feugiat sapien eget egestas tincidunt. Phasellus vulputate, urna sit amet scelerisque fermentum, neque nulla pellentesque risus, non convallis neque lorem a nisi. In molestie justo feugiat rhoncus bibendum. Quisque mollis aliquet nibh. Suspendisse potenti. In dictum nisl vitae varius cursus. Praesent gravida at orci ut consequat. Sed egestas adipiscing ullamcorper.</p>
    <p>Aliquam varius ipsum consequat justo lacinia, eleifend ultricies urna pulvinar. Donec tempor non libero vel lobortis. Praesent a orci arcu. Fusce egestas vehicula sem vel porttitor. Cras vel ultrices urna, sit amet imperdiet erat. Nunc neque augue, venenatis eget accumsan sed, commodo at ligula. Cras imperdiet blandit erat, id porta est dignissim a. In nec ipsum ac quam sodales pulvinar. Vivamus iaculis tristique risus a pharetra. In hac habitasse platea dictumst. Nam tempor venenatis dolor, nec commodo urna ultricies non. Aenean sit amet justo sagittis ligula sodales cursus. Nam cursus augue et imperdiet vehicula. Nunc tempor diam sit amet gravida gravida. Interdum et malesuada fames ac ante ipsum primis in faucibus.</p>
    <p>Fusce sodales nunc a orci rutrum gravida. Quisque quam neque, volutpat id eleifend vel, aliquam et nunc. Duis rhoncus magna sed sem tristique, sit amet adipiscing eros vehicula. Nullam dictum a ante nec venenatis. Quisque mattis vehicula augue, et consectetur mi euismod eu. Etiam quam tellus, vulputate in gravida id, ullamcorper at ipsum. Aenean quis tellus ut risus ultrices egestas.</p>
  </main>

  <footer class="site-footer">
    <nav class="footer-nav">
      <a style="left:247px">Home</a>
      <a style="left:346px">Menu</a>
      <a style="left:446px">Contact</a>
      <a style="left:556px">Calendar</a>
      <a style="left:674px">Press</a>
      <a style="left:771px">Gallery</a>
    </nav>
    <div class="footer-rule"></div>
    <p class="copyright">Copyright © 2014 La Paloma Taberna. &nbsp;All rights reserved.</p>
  </footer>
</div>
</body>
</html>
```